Professional WordPress Website Design & Development for IT Consulting Company (Quennor)

We are an IT consulting company (Quennor) based in Germany and are looking for a professional, modern and scalable WordPress website design INCLUDING full coding (WordPress theme/template).

IMPORTANT:
We do NOT want only a design (eg Photoshop files).
We want a fully working, coded WordPress website that we can host and manage ourselves.

The uploaded files (PowerPoint, HTML, logo) are ONLY for rough orientation.
They do NOT represent the final structure but give an idea of our visual style.

---

## COMPANY STRUCTURE (IMPORTANT)

Currently we operate as:

* Quennor UG (limited liability)

Planned structure:

* Quennor Operations GmbH (main operating company)
* Quennor Holding GmbH
* optionally later: Quennor Capital GmbH

The website should be designed as a scalable group website, but currently focus on the main brand "Quennor".

---

## BUSINESS FOCUS (IMPORTANT)

Our main business is:
→ Managed Services (core focus)

Additional areas:

* IT Infrastructure (VMware, Citrix, Hyper-V)
* Windows Server/Client environments
* Cloud & Hybrid solutions
* Network, Firewall, VPN
* Data center operations, migrations and rollouts

The website should clearly communicate:
→ reliability, scalability, enterprise-level service quality

---

## DESIGN STYLE & VISUAL DIRECTION

We like the design direction from our uploaded PowerPoint.

IMPORTANT:

* We especially like the green checkered/grid-style background with dark/black gradient
* This style should be used as inspiration
* Colors: green + dark/black + modern IT style

Design should be:

* modern
* clean
* professional
* enterprise-level
* trustworthy
* not playful or overloaded

---

## TECHNICAL REQUIREMENTS

* WordPress (self-hosted)
* Full source code delivery (no proprietary lock-in)
* Custom theme or clean reusable theme
* Editable without developer
* Multilingual: German, English, Polish
* SEO-friendly
* Fast performance
* GDPR/DSVO compliant contact form

---

## RESPONSIVE DESIGN & ACCESSIBILITY

Must be optimized for:

* Desktop
* Tablet
* Mobile

Layout must adapt automatically.

Accessibility:

* Clear typography
* Good contrast
* Easy navigation
* Mobile-friendly usability

Mobile experience must be fully functional and professional.

---

## STRUCTURE (NO ONE-PAGE WEBSITE)

We want a structured website with pages and subpages.

MAIN NAVIGATION (HEADER):

* Home
* Managed Services (MAIN FOCUS)
* Services
* Solutions / Expertise
* Projects / News
* Resources
* Careers
* Company
* Contact

SUBNAVIGATION / SUBPAGES (examples):

Managed Services:

* Overview
* Service Models
* SLAs & Support
* Monitoring & Operations

Services:

* VMware
* Citrix
* Hyper-V
* Windows Server / Client
* SCCM / Intune
* Network / Firewall / VPN

Solutions:

* Data Center
* Cloud / Hybrid
* Migration Projects
* Security / Zero Trust

Projects / News:

* Projects
* Opportunities
* Articles

Resources:

* Available Experts
* Freelancer / Partner
* Internal Staff

Careers:

* Open Positions
* Freelancer Opportunities

Company:

* About Us
* Group Structure
* Values
* References

---

## HEADER / FOOTER STRUCTURE

HEADER:

* Sticky header (always visible)
* Main navigation with dropdowns or mega menu
* Clean, structured layout

FOOTER:

* Legal pages (Imprint, Privacy, Terms)
* Contact information
* Possibly quick links
* Consistent across all pages

---

## SPECIAL FEATURES

1. PROJECT / NEWS SYSTEM

* publish projects
* project opportunities
* articles

2. RESOURCE SYSTEM

* freelancers
* partners
* internal staff

With:

* skills
* availability
* role
* location
* language

---

## IMAGES, ICONS & LICENSING

Stock images (eg iStock) may be used as placeholders.

IMPORTANT:

* We will purchase final licenses ourselves
* No Google images or unknown sources

Icons and illustrations are welcome but must be properly licensed.

At delivery:

* Full asset list required (images, icons, sources, licenses)

---

## DELIVERABLES

We expect:

* Fully working WordPress website
* Full source code
* Installation instructions
* Plugin list
* No hidden dependencies
* No forced subscriptions
* Full usage rights

---

## IMPORTANT

We want to pay ONCE and fully own everything.

---

## LANGUAGES

Content will be managed by us:

* German
* English
* Polish

---

## FILES

Uploaded files are only for inspiration.

---

We are looking for a long-term, scalable and professional solution suitable for enterprise customers.
Updates

Additional update regarding interactions, hover effects and animations:

HOVER EFFECTS

We would like to include subtle and modern hover effects across the website:

Cards (eg Open Positions, Projects): → slight green glow on hover → minimal lift effect (approx. 2–4px)

Navigation (header): → hover color should be green (NOT orange)

Footer links (Imprint, Privacy, Terms): → slightly brighter on hover

Social icons (LinkedIn, XING, Gigstrelo): → subtle glow and slight scale on hover

IMPORTANT: All hover effects must be consistent, clean and not exaggerated.

ACTIVE STATE (VERY IMPORTANT)

Navigation elements must clearly show when they are active (current page).

This applies to:

Header navigation footer left

Behavior:

Active links should remain highlighted (eg green color and/or subtle underline) Users should always clearly see which page they are currently on

IMPORTANT: Active and hover states must be visually consistent across the entire website.

ANIMATIONS / MICRO INTERACTIONS

The website should not feel static.

We would like subtle and professional animations, such as:

smooth transitions between elements minimal background movement (very subtle) soft UI interactions

IMPORTANT: No heavy, flashy or distracting animations.

The goal is a high-end, enterprise-level feel.

COUNTERS / KEY METRICS

We want animated key numbers, for example:

150+ clients 10+ years experience 24/7 support 99.9% uptime

Behavior:

numbers should count up when they come into view (on scroll) fast and smoothly (approx. 0. 5–1 seconds) animation should trigger only once

Overall goal: A modern, dynamic and high-quality website with subtle interactions, not a flashy or overloaded design.

Hi everyone,

I have uploaded additional reference files to give you a clearer idea of the direction we are aiming for.

IMPORTANT: These files are only meant as inspiration and guidance – they are NOT strict templates that must be copied 1:1.

What we particularly like:

Dark / black + green design Subtle grid / tech background (as seen in the PowerPoint) Clean, modern and professional enterprise IT style Structured layout (no one-page scrolling) LANGUAGE FLAGS (IMPORTANT UPDATE)

Please adjust the language selection as follows:

Order:

German (DE) English (EN) Polish (PL)

For ENGLISH: We do NOT want a standard flag.

Instead, please create a combined UK/US flag:

Diagonally split design One side showing the UK flag The other side showing the US flag

This should look clean and professional (not playful).

FOOTER (IMPORTANT)

Footer should be:

Minimal and clean (not large or heavy) Positioned at the very bottom

Include:

Legal Notice / Imprint / Privacy Policy / Data Protection / Terms and Conditions / Terms

And: © Quennor UG

Social icons:

LinkedIn XING Gigstrelo

Please remove:

Facebook Twitter Instagram LAYOUT NOTE

Please avoid duplicate sections (eg "About Us" appearing multiple times).

We prefer a clean and structured layout with clear sections.

Thank you very much – looking forward to your designs!

Ich brauche zusätzliche Tage um durchzusehen

Target Market(s)

Enterprise and mid-sized companies, especially in automotive, finance, technology and IT infrastructure environments.

Industry/Entity Type

IT Consulting / Managed Services / Enterprise IT

Coding

Coded - Design and coding required

Font styles to use
Sans Serif

Colors
0094D4
00A9DD
6FCCEA
C7EBF8
E9F6FB
00AB8E
00BBA5
67D7C9
C6EFE9
E9F9F6
59FF00
82FF00
B8FF75
E3FFCB
F4FFEA

Requirements
Must have
• - Fully coded WordPress website (not just design) - Self-hosted, no dependency on designer - Responsive (desktop, tablet, mobile) - Multilingual (German, English, Polish) - Editable without developer - Clean, modern enterprise design - Structured navigation with subpages (no one-page website) - GDPR-compliant contact form - Scalable structure for future company expansion (group structure)
Nice to have
• - Subtle modern animations (not overloaded) - Mega menu or structured dropdown navigation - Clean icon set and optional illustrations - Reusable page templates - Fast loading performance - SEO-friendly structure - Team presentation with profiles (management, internal staff, technical roles) - Integration of social links (LinkedIn, Xing, Gigstrelo)
Should not have
• - No one-page scrolling website - No overly colorful or playful design - No outdated or generic templates - No confusing or complex navigation - No cheap-looking stock-heavy layouts - No dependency on proprietary builders or subscriptions

```html
<!DOCTYPE html>
<html lang="en">
<head>
<meta charset="utf-8">
<title>Quennor – Services</title>
<link rel="stylesheet" href="https://fonts.googleapis.com/css2?family=Inter:wght@400;500&family=Inter+Tight:wght@400;700&family=JetBrains+Mono:wght@400;500&display=swap">
<style>
  :root {
    --bg: #0b0c0e;
    --grid: rgba(255,255,255,0.035);
    --white: #f4f5f6;
    --muted: #9a9ea6;
    --dim: #8a8d93;
    --green: #66d42a;
    --brand: #3d6e5a;
    --border: #2a2c31;
    --photo-a: #1c1d1f;
    --photo-b: #4a4b4d;
  }
  * { margin: 0; padding: 0; box-sizing: border-box; }
  html, body { width: 1200px; height: 2487px; overflow: hidden; }
  body {
    background: var(--bg);
    color: var(--white);
    font-family: "Inter", sans-serif;
    position: relative;
  }
  .grid-bg {
    position: absolute; left: 0; top: 220px; width: 1100px; height: 800px;
    background-image:
      linear-gradient(to right, var(--grid) 1px, transparent 1px),
      linear-gradient(to bottom, var(--grid) 1px, transparent 1px);
    background-size: 166px 166px;
    background-position: 0 -31px;
    -webkit-mask-image: linear-gradient(to bottom, transparent, #000 20%, #000 70%, transparent);
            mask-image: linear-gradient(to bottom, transparent, #000 20%, #000 70%, transparent);
  }
  .site-header {
    position: absolute; left: 66px; right: 95px; top: 40px; height: 100px;
    display: flex; justify-content: space-between; align-items: flex-start;
  }
  .brand {
    display: flex; align-items: center; gap: 22px;
    font-family: "Inter", sans-serif; font-weight: 500;
    font-size: 70px; line-height: 90px; color: var(--brand); letter-spacing: -0.01em;
  }
  .brand-mark { width: 58px; height: 58px; background: var(--brand); border-radius: 6px; }
  .menu-toggle { margin-top: 22px; }
  .services-intro { position: absolute; left: 66px; top: 398px; width: 1000px; }
  .eyebrow {
    font-family: "JetBrains Mono", monospace; font-weight: 500;
    font-size: 31px; letter-spacing: 0.14em; color: var(--green);
  }
  .section-title {
    margin-top: 38px;
    font-family: "Inter Tight", sans-serif; font-weight: 700;
    font-size: 110px; line-height: 1; letter-spacing: -0.03em;
  }
  .lead {
    margin-top: 74px; width: 960px;
    font-size: 35px; line-height: 63px; color: var(--muted);
  }
  .service { position: absolute; left: 66px; top: 1200px; width: 966px; }
  .service-meta { display: flex; align-items: center; gap: 36px; }
  .service-num { font-family: "JetBrains Mono", monospace; font-size: 30px; color: var(--dim); }
  .service-title {
    margin-top: 44px;
    font-family: "Inter Tight", sans-serif; font-weight: 400;
    font-size: 92px; line-height: 100px; letter-spacing: -0.02em;
  }
  .service-title .accent { color: var(--green); }
  .service-text { margin-top: 66px; font-size: 35px; line-height: 63px; color: var(--muted); }
  .btn {
    margin-top: 60px; width: 442px; height: 136px;
    border: 2px solid var(--border); border-radius: 30px;
    display: flex; align-items: center; justify-content: center; gap: 28px;
    font-size: 40px; font-weight: 500; color: var(--white);
  }
  .service-photo {
    position: absolute; left: 68px; top: 2105px; width: 964px; height: 420px;
    border-radius: 28px;
    background: radial-gradient(ellipse at 60% 60%, var(--photo-b), var(--photo-a) 70%);
  }
</style>
</head>
<body>
  <div class="grid-bg"></div>

  <header class="site-header">
    <div class="brand"><span class="brand-mark"></span>Quennor</div>
    <svg class="menu-toggle" width="52" height="50" viewBox="0 0 52 50" aria-label="Menu">
      <g stroke="#fff" stroke-width="5" stroke-linecap="round">
        <line x1="3" y1="4" x2="49" y2="4"/><line x1="3" y1="26" x2="49" y2="26"/><line x1="3" y1="48" x2="49" y2="48"/>
      </g>
    </svg>
  </header>

  <section class="services-intro">
    <p class="eyebrow">SERVICES</p>
    <h1 class="section-title">WHAT WE DELIVER</h1>
    <p class="lead">From day-to-day operations to complex transformations, we provide end-to-end IT services that keep your business running and growing.</p>
  </section>

  <article class="service">
    <div class="service-meta">
      <svg width="62" height="62" viewBox="0 0 62 62" aria-hidden="true">
        <g fill="none" stroke="var(--green)" stroke-width="4.5">
          <rect x="3" y="3" width="56" height="24" rx="6"/>
          <rect x="3" y="35" width="56" height="24" rx="6"/>
        </g>
        <circle cx="13" cy="15" r="2.5" fill="var(--green)"/>
        <circle cx="13" cy="47" r="2.5" fill="var(--green)"/>
      </svg>
      <span class="service-num">01</span>
    </div>
    <h2 class="service-title">MANAGED<br>SERVICES.<br><span class="accent">ALWAYS ON.</span></h2>
    <p class="service-text">We run your IT day-to-day: monitoring, patching, backups, and incident response—with clear SLAs.</p>
    <a class="btn">Learn more
      <svg width="34" height="30" viewBox="0 0 34 30" aria-hidden="true"><g fill="none" stroke="#fff" stroke-width="3.5" stroke-linecap="round" stroke-linejoin="round"><line x1="3" y1="15" x2="30" y2="15"/><polyline points="18,3 30,15 18,27"/></g></svg>
    </a>
  </article>

  <div class="service-photo" role="img" aria-label="Black and white photo of hands at a laptop in front of server monitoring screens"></div>
</body>
</html>
```